Roofing Contractor business card redesign

I want to redesign my business card with a fresh, eye catching concept

Target Market(s)

Residential Roofing Clients, potential employees, and subcontractors.

Industry/Entity Type

Business

Colors

Designer to choose colors to be used in the design.

Requirements
Nice to have
• I just want something that's more pleasing to the eye. You can use a combination of either / or of my logos.

```html
<!DOCTYPE html>
<html lang="en">
<head>
<meta charset="utf-8">
<title>Stout Crew – Business Card</title>
<link href="https://fonts.googleapis.com/css2?family=Oswald:wght@500;700&family=Work+Sans:wght@400&family=Open+Sans:wght@700&display=swap" rel="stylesheet">
<style>
  :root {
    --orange: #f4821f;
    --brown: #4a1510;
    --ink: #2b2b2b;
    --paper: #ffffff;
    --backdrop: #2a2a2a;
  }
  * { margin: 0; padding: 0; box-sizing: border-box; }
  html, body { width: 1200px; height: 930px; overflow: hidden; }
  body { background: var(--backdrop); position: relative; font-family: "Work Sans", sans-serif; }

  .card {
    position: absolute; left: 278px; width: 645px; height: 368px;
    border-radius: 24px; overflow: hidden;
  }
  .card--front { top: 76px; background: var(--paper); }
  .card--back { top: 486px; background: var(--orange); }

  .card__wave { position: absolute; inset: 0; width: 100%; height: 100%; }

  .person { position: absolute; left: 38px; top: 132px; }
  .person__name {
    font-family: "Oswald", sans-serif; font-weight: 500; font-size: 30px;
    letter-spacing: 1px; color: var(--orange); line-height: 36px;
  }
  .person__role { font-size: 17px; line-height: 20px; color: var(--ink); }

  .divider { position: absolute; left: 38px; top: 223px; width: 570px; height: 1px; background: var(--brown); }

  .contacts { position: absolute; left: 38px; top: 240px; list-style: none; }
  .contacts li { display: flex; align-items: center; font-size: 17px; line-height: 20px; color: var(--ink); }
  .contacts svg { width: 12px; height: 12px; margin-right: 13px; fill: none; stroke: var(--orange); stroke-width: 1.6; }

  .address { position: absolute; right: 37px; top: 260px; text-align: right; font-size: 17px; line-height: 20px; color: var(--ink); font-style: normal; }

  .brand-mini { position: absolute; left: 488px; top: 32px; width: 120px; text-align: center; }
  .brand-mini__mark { width: 100px; height: 100px; margin: 0 auto 8px; border-radius: 50%; background: var(--orange); }
  .brand-mini__name { font-family: "Oswald", sans-serif; font-weight: 700; font-size: 26px; line-height: 30px; color: var(--brown); }

  .brand { position: absolute; left: 0; right: 0; top: 108px; display: flex; justify-content: center; align-items: center; gap: 10px; }
  .brand__name { font-family: "Oswald", sans-serif; font-weight: 700; font-size: 74px; line-height: 84px; color: var(--brown); }
  .brand__mark { width: 94px; height: 94px; border-radius: 50%; background: var(--brown); }
  .brand__tagline {
    position: absolute; left: 0; right: 0; top: 220px; text-align: center;
    font-family: "Open Sans", sans-serif; font-weight: 700; font-size: 32px; color: var(--brown);
  }
</style>
</head>
<body>
  <section class="card card--front">
    <div class="brand-mini">
      <div class="brand-mini__mark"></div>
      <div class="brand-mini__name">Stout Crew</div>
    </div>

    <div class="person">
      <h1 class="person__name">MARK DELLAN</h1>
      <p class="person__role">Halvor Certified Roof Inspector</p>
      <p class="person__role">Licensed Property Adjuster</p>
    </div>

    <div class="divider"></div>

    <ul class="contacts">
      <li><svg viewBox="0 0 12 12"><path d="M2 1 L4 1 L5 4 L3.5 5 Q5 8 7 8.5 L8 7 L11 8 L11 10 Q6 11 2 6 Q1 3 2 1 Z"/></svg>(555) 014-2200</li>
      <li><svg viewBox="0 0 12 12"><rect x="3" y="0.8" width="6" height="10.4" rx="1"/><line x1="5" y1="9" x2="7" y2="9"/></svg>(555) 016-7381</li>
      <li><svg viewBox="0 0 12 12"><rect x="0.8" y="2.5" width="10.4" height="7"/><path d="M0.8 2.5 L6 6.5 L11.2 2.5"/></svg>mark@stoutcrewtx.com</li>
    </ul>

    <address class="address">4410 Alder Lane<br>Suite 108 Fairview, TX 75000</address>

    <svg class="card__wave" viewBox="0 0 645 368" preserveAspectRatio="none" aria-hidden="true">
      <path d="M0 336 C150 374 300 352 470 320 C560 306 610 330 645 352 L645 368 L0 368 Z" fill="var(--orange)"/>
      <path d="M12 340 C160 372 300 350 470 318 C560 303 610 322 636 344" fill="none" stroke="var(--brown)" stroke-width="4"/>
    </svg>
  </section>

  <section class="card card--back">
    <div class="brand">
      <span class="brand__name">Stout</span>
      <span class="brand__mark"></span>
      <span class="brand__name">Crew</span>
    </div>
    <p class="brand__tagline">General Contractors, Inc.</p>
  </section>
</body>
</html>
```